Lanternfield Parking Lot Vision Flags

Size: 3 banners - 2' x 4' banners (portrait)
Design: all the same design with different text
text on banner 1: Building Solid Lives
text on banner 2: Come. Hear. Do. Luke 6
text on banner 3: Worship Center
Details: Use the colors red, white and black and use the h logo attached
Make white the main color (not too much black and not too much red) Keep design simple - not a lot of different textures - more "quince like"

Target Market(s)

30-50 year olds

Industry/Entity Type

Parking

Font styles to use
Sans Serif

Colors
ec1f27
fbfbfb
1b1b1b

Requirements
Must have
• Logo and the colors red white and black
Nice to have
• simple - clean - cool
Should not have
• busy backgrounds and textures

```html
<!DOCTYPE html>
<html lang="en">
<head>
<meta charset="utf-8">
<title>Parking Lot Vision Flags</title>
<link rel="stylesheet" href="https://fonts.googleapis.com/css2?family=Roboto+Condensed:wght@700;900&display=swap">
<style>
  :root {
    --brand-red: #ec1f27;
    --brand-white: #fbfbfb;
    --brand-black: #1b1b1b;
    --stage: #ebe8e3;
    --texture-light: #ffffff;
    --texture-shade: #e6e6e6;
  }
  * { margin: 0; padding: 0; box-sizing: border-box; }
  html, body {
    width: 1200px;
    height: 750px;
    overflow: hidden;
    background: var(--stage);
  }
  .flag-set {
    position: relative;
    width: 1200px;
    height: 750px;
  }
  .flag {
    position: absolute;
    top: 96px;
    width: 300px;
    height: 600px;
    background: var(--brand-white);
    box-shadow: 0 2px 6px rgba(0,0,0,0.12);
    overflow: hidden;
  }
  .flag--lives { left: 88px; }
  .flag--come { left: 457px; }
  .flag--worship { left: 821px; }
  .flag__backdrop {
    position: absolute;
    inset: 0;
    background: linear-gradient(170deg, var(--texture-light) 0%, var(--brand-white) 35%, var(--texture-shade) 100%);
  }
  .flag__message {
    position: absolute;
    top: 100px;
    left: 0;
    right: 0;
    text-align: center;
    font-family: "Roboto Condensed", "Arial Narrow", sans-serif;
    font-weight: 900;
    color: var(--brand-black);
    font-size: 62px;
    line-height: 68px;
    letter-spacing: 2.5px;
  }
  .flag__reference {
    display: block;
    margin-top: 20px;
    font-size: 42px;
    line-height: 46px;
    font-weight: 900;
    letter-spacing: 2.5px;
  }
  .flag__brand {
    position: absolute;
    top: 450px;
    left: 0;
    right: 0;
    display: flex;
    align-items: center;
    justify-content: center;
    gap: 8px;
    font-family: "Roboto Condensed", "Arial Narrow", sans-serif;
    font-weight: 900;
    font-size: 24px;
    letter-spacing: 1px;
    color: var(--brand-red);
  }
  .flag__brand-mark {
    width: 16px;
    height: 16px;
    border-radius: 50%;
    background: var(--brand-red);
  }
</style>
</head>
<body>
  <main class="flag-set">
    <section class="flag flag--lives">
      <div class="flag__backdrop" role="img" aria-label="Soft white curved grid texture"></div>
      <h2 class="flag__message">Building<br>Solid<br>Lives</h2>
      <div class="flag__brand"><span class="flag__brand-mark"></span>Lanternfield</div>
    </section>
    <section class="flag flag--come">
      <div class="flag__backdrop" role="img" aria-label="Soft white curved grid texture"></div>
      <h2 class="flag__message">Come.<br>Hear.<br>Do.<span class="flag__reference">Luke 6</span></h2>
      <div class="flag__brand"><span class="flag__brand-mark"></span>Lanternfield</div>
    </section>
    <section class="flag flag--worship">
      <div class="flag__backdrop" role="img" aria-label="Soft white curved grid texture"></div>
      <h2 class="flag__message">Worship<br>Center</h2>
      <div class="flag__brand"><span class="flag__brand-mark"></span>Lanternfield</div>
    </section>
  </main>
</body>
</html>
```